Photography Price List DL flyer

In need of a double sided DL flyer to list prices for a photography business that is in the real estate industry. Will need to include logo and be themed to match. Price details and contact information are in the pdf attached.

Below are links to the logo and photos that can be used on the flyer.

Logo
https://www.parcelnook.net/s/q7mwd2kfp0zltab/LogoFiles.zip?dl=0

Photos
https://www.parcelnook.net/s/h3vtr9gkw1jenoy/Website_Images.zip?dl=0
Updates

Sorry people the photo examples I put the wrong link. I have fixed it in the brief but the proper link is: https://www.parcelnook.net/s/h3vtr9gkw1jenoy/Website_Images.zip?dl=0

Also dimensions of a DL are 210mm x 99mm + 3m bleed. Thanks

Target Market(s)

Real estate agents

Industry/Entity Type

Business

Requirements
Must have
• Price lists and contact information

```html
<!DOCTYPE html>
<html lang="en">
<head>
<meta charset="utf-8">
<title>Brightlane Photos – DL Price Flyer</title>
<link href="https://fonts.googleapis.com/css2?family=Montserrat:wght@400;500;600&display=swap" rel="stylesheet">
<style>
  :root {
    --backdrop: #e4e2df;
    --card: #ffffff;
    --coral: #ee6a6c;
    --lime: #a2cc5a;
    --ink: #3a3a3a;
    --photo-deck: linear-gradient(160deg, #dfe8ee 0%, #6f9b4e 40%, #d9d6cf 62%, #4ab3d2 100%);
    --photo-dining: linear-gradient(140deg, #e9ecec 0%, #b8c4b2 45%, #c48a52 75%, #e4e4e4 100%);
    --photo-verandah: linear-gradient(170deg, #9aa496 0%, #3f8a3a 40%, #6fae55 60%, #3b4a66 100%);
  }
  * { box-sizing: border-box; margin: 0; padding: 0; }
  html, body { width: 1200px; height: 1000px; overflow: hidden; }
  body {
    background: var(--backdrop);
    font-family: "Montserrat", sans-serif;
    color: var(--ink);
    position: relative;
  }
  .flyer-side {
    position: absolute;
    background: var(--card);
    box-shadow: 0 4px 14px rgba(0,0,0,0.18);
  }
  .flyer-front { left: 202px; top: 98px; width: 831px; height: 393px; }
  .flyer-back  { left: 204px; top: 510px; width: 829px; height: 388px; }
  .photo { position: absolute; }
  .photo-deck     { left: 16px; top: 18px; width: 471px; height: 356px; background: var(--photo-deck); }
  .photo-dining   { left: 503px; top: 18px; width: 314px; height: 235px; background: var(--photo-dining); }
  .photo-verandah { left: 18px; top: 18px; width: 468px; height: 354px; background: var(--photo-verandah); }

  .brand {
    position: absolute;
    display: flex;
    align-items: center;
    gap: 12px;
    font-weight: 600;
    color: var(--coral);
    letter-spacing: 0.06em;
    text-transform: uppercase;
    white-space: nowrap;
  }
  .brand-mark { border-radius: 50%; background: var(--coral); flex: none; }
  .brand-front { left: 505px; top: 289px; width: 300px; justify-content: space-between; font-size: 18px; }
  .brand-front .brand-mark { width: 60px; height: 60px; }
  .brand-overlay { left: 48px; top: 300px; font-size: 17px; }
  .brand-overlay .brand-mark { width: 38px; height: 38px; }

  .price-list {
    position: absolute;
    right: 26px;
    top: 22px;
    text-align: right;
    font-size: 14.5px;
    line-height: 18px;
  }
  .price-list h1 {
    font-size: 22px;
    font-weight: 600;
    color: var(--coral);
    line-height: 26px;
  }
  .price-list h2 {
    font-size: 14.5px;
    font-weight: 500;
    color: var(--lime);
    line-height: 18px;
    margin-top: 17px;
  }
  .price-list h1 + h2 { margin-top: 0; }
  .price-list ul { list-style: none; }
</style>
</head>
<body>
  <section class="flyer-side flyer-front">
    <div class="photo photo-deck" role="img" aria-label="Photograph of a modern home balcony with glass balustrade overlooking a pool and bushland"></div>
    <div class="photo photo-dining" role="img" aria-label="Photograph of a bright open-plan dining room with timber table and sliding glass doors"></div>
    <div class="brand brand-front"><span>Brightlane Photos</span><span class="brand-mark"></span></div>
  </section>

  <section class="flyer-side flyer-back">
    <div class="photo photo-verandah" role="img" aria-label="Photograph of a covered timber verandah with outdoor dining set surrounded by tropical garden"></div>
    <div class="brand brand-overlay"><span>Brightlane Photos</span><span class="brand-mark"></span></div>

    <div class="price-list">
      <h1>Prices</h1>
      <h2>Photography</h2>
      <ul>
        <li>10 images $149</li>
        <li>12 – 15 images $179</li>
        <li>20+ images $229</li>
      </ul>
      <h2>Twilight</h2>
      <ul>
        <li>Add $100 to image package</li>
        <li>Floorplans – $49</li>
      </ul>
      <h2>Video</h2>
      <ul>
        <li>30 seconds $150</li>
        <li>60 seconds $200</li>
        <li>2 minutes $300</li>
      </ul>
      <h2>Contact Details</h2>
      <ul>
        <li>mobile : 0400 555 123</li>
        <li>web: brightlanephotos.com.au</li>
        <li>email: info@brightlanephotos.com.au</li>
      </ul>
    </div>
  </section>
</body>
</html>
```